Auto Repair Shop offering Free Oil Change for a Year Contest

Bremly Gearworks & Auto Care www.visitbremly.example needs a 1 page information gathering site where contest entrants will be directed after clicking on a banner we have already designed. We need this page to collect their Name, Address, Phone, email, and year make and model of the vehicle they drive. It must be simple and clean looking and hold their interest so they actually sign up. On the back end, I would like this information to be collected placed into an excel file and emailed to us one time a day. We do not have much time so Fluent English is a must. I have supplied our current URL because I would like this page to have the same look and feel as our current webpage using our red white and blue colors and our logo.
Updates

Project Deadline Extended
Reason: I would like more design input, so I am extending the deadline.

Target Market(s)

A wide spectrum, People who drive cars and need them repaired. Typically a customer will be someone who had a 7-10 year old car.

Industry/Entity Type

Shop

Requirements
Must have
• ease of use and appear simple to enter contest. Data entry features that support excel.
Nice to have
• design that would also be able to be used on an iphone or android friendly

```html
<!DOCTYPE html>
<html lang="en">
<head>
<meta charset="utf-8">
<title>Bremly Gearworks &amp; Auto Care — Free Oil Change for a Year</title>
<link rel="stylesheet" href="https://fonts.googleapis.com/css2?family=Mulish:wght@600;700&family=Open+Sans:ital,wght@0,400;0,600;1,400&display=swap">
<style>
  :root {
    --brand-red: #c8101a;
    --brand-red-dark: #9e0a10;
    --header-top: #2a2b2e;
    --header-bottom: #111214;
    --nav-bg: #1c1d20;
    --nav-divider: #3a3b3f;
    --page-bg: #e4e5e8;
    --panel-bg: rgba(255, 255, 255, 0.55);
    --panel-border: #d9d9dc;
    --ink: #1e1e1e;
    --placeholder: #6a6a6a;
    --field-top: #ffffff;
    --field-bottom: #ececee;
    --white: #ffffff;
    --reset-top: #8b8c8f;
    --reset-bottom: #505155;
  }
  * { box-sizing: border-box; margin: 0; padding: 0; }
  html, body { width: 1200px; height: 1001px; overflow: hidden; }
  body {
    position: relative;
    background: var(--page-bg);
    font-family: "Open Sans", Arial, sans-serif;
    color: var(--ink);
  }
  .site-header {
    position: absolute; left: 0; top: 0; width: 1200px; height: 148px;
    background: linear-gradient(var(--header-top), var(--header-bottom));
    border-top: 8px solid var(--brand-red);
  }
  .brand {
    position: absolute; left: 73px; top: 44px;
    display: flex; align-items: center; gap: 12px;
    font-family: "Mulish", Arial, sans-serif; font-weight: 700;
    font-size: 24px; color: var(--white); line-height: 1.1; width: 260px;
  }
  .brand-mark { width: 18px; height: 18px; background: var(--brand-red); flex: none; }
  .main-nav {
    position: absolute; left: 484px; top: 84px; width: 644px; height: 55px;
    background: var(--nav-bg); border-radius: 5px 5px 0 0;
    display: flex;
  }
  .main-nav a {
    flex: 1 1 auto; display: flex; align-items: center; justify-content: center;
    color: var(--white); text-decoration: none; font-weight: 600; font-size: 16px;
    border-left: 1px solid var(--nav-divider);
  }
  .main-nav a:first-child { border-left: 0; }
  .hero-photo {
    position: absolute; left: 0; top: 148px; width: 1200px; height: 853px;
    background: radial-gradient(ellipse 620px 300px at 600px 560px, #9a9b9f 0%, #c9cacd 45%, #eeeff1 85%);
  }
  .form-panel {
    position: absolute; left: 68px; top: 177px; width: 1067px; height: 840px;
    background: var(--panel-bg); border-radius: 6px;
  }
  .form-card {
    position: absolute; left: 27px; top: 27px; width: 1017px; height: 768px;
    border: 1px solid var(--panel-border); border-radius: 5px;
  }
  .form-title {
    position: absolute; left: 33px; top: 24px;
    font-family: "Mulish", Arial, sans-serif; font-weight: 700; font-size: 27px;
  }
  .form-intro {
    position: absolute; left: 33px; top: 64px;
    color: var(--brand-red); font-weight: 600; font-size: 14px;
  }
  .form-divider {
    position: absolute; left: 31px; top: 102px; width: 951px; height: 1px;
    background: #c4c4c7;
  }
  .entry-form label {
    position: absolute; left: 44px;
    font-family: "Mulish", Arial, sans-serif; font-weight: 700; font-size: 16px;
    line-height: 22px;
  }
  .entry-form .field {
    position: absolute; left: 213px; height: 42px;
    border: 1px solid #d2d2d5; border-radius: 5px;
    background: linear-gradient(var(--field-top), var(--field-bottom));
    padding: 0 15px; font-family: "Open Sans", Arial, sans-serif;
    font-style: italic; font-size: 14px; color: var(--ink);
  }
  .entry-form .field::placeholder { color: var(--placeholder); }
  .field-wide { width: 534px; }
  .field-short { width: 314px; }
  .entry-form textarea.field { height: 111px; padding-top: 10px; resize: none; }
  .button {
    position: absolute; top: 559px; height: 42px; border-radius: 5px; border: 0;
    color: var(--white); font-family: "Open Sans", Arial, sans-serif;
    font-weight: 600; font-size: 15px;
  }
  .button-submit { left: 218px; width: 123px; background: linear-gradient(#e01b24, var(--brand-red-dark)); }
  .button-reset { left: 391px; width: 122px; background: linear-gradient(var(--reset-top), var(--reset-bottom)); }
  .or-text {
    position: absolute; left: 356px; top: 570px;
    font-family: "Mulish", Arial, sans-serif; font-weight: 700; font-size: 14px;
  }
</style>
</head>
<body>
  <header class="site-header">
    <div class="brand"><span class="brand-mark"></span><span>Bremly Gearworks &amp; Auto Care</span></div>
    <nav class="main-nav">
      <a href="#">Home</a><a href="#">Services</a><a href="#">Staff</a><a href="#">Reviews</a><a href="#">Links</a><a href="#">Affilation</a><a href="#">Gallery</a>
    </nav>
  </header>

  <div class="hero-photo" role="img" aria-label="Faded photo of a white sports car seen from the rear"></div>

  <main class="form-panel">
    <section class="form-card">
      <h1 class="form-title">Fill Information Form</h1>
      <p class="form-intro">Win a Free Oil Change for a Year! Please enter your Name, Address, Phone, Email, year make &amp; Model.</p>
      <div class="form-divider"></div>
      <form class="entry-form">
        <label for="full-name" style="top:133px">Your Full Name:</label>
        <input class="field field-wide" id="full-name" placeholder="type your full name" style="top:128px">

        <label for="email" style="top:193px">Your Email Address:</label>
        <input class="field field-wide" id="email" type="email" placeholder="type your email address" style="top:188px">

        <label for="address" style="top:258px">Your Address:</label>
        <textarea class="field field-wide" id="address" placeholder="type your address" style="top:253px"></textarea>

        <label for="year" style="top:388px">Year Make:</label>
        <input class="field field-short" id="year" placeholder="type your year" style="top:383px">

        <label for="model" style="top:442px">Model of Vehicle:</label>
        <input class="field field-short" id="model" placeholder="type your vehicle model" style="top:437px">

        <label for="phone" style="top:496px">Your Phone:</label>
        <input class="field field-short" id="phone" type="tel" placeholder="type your phone number" style="top:491px">

        <button type="submit" class="button button-submit">Submit Now</button>
        <span class="or-text">Or</span>
        <button type="reset" class="button button-reset">Reset Now</button>
      </form>
    </section>
  </main>
</body>
</html>
```